Business card for our large format printing and installation business

We want a professional looking business card for our business. We manufacture and install Signs.

On the back of the card add this info
Large Format Graphics Printing & Installations, Event Graphics, Banners, Posters, Vehicle Fleet Graphics, Boat Wraps, Wall Murals, Decals,Displays,Signs,Plaques,Digital Signs

On the Front of the card add the Tallmoor Signs logo, plus On the back of the card add the Orange Tallmoor Wraps logo. The 2 vector logos are attached to the design brief.

Target Market(s)

Local business owners

Contact Information for Business Card

Colors
f37122
f68d4e
f9ba93

Requirements
Must have
• On the Front of the card add the Tallmoor Signs logo, plus On the back of the card add the Orange Tallmoor Wraps logo. The 2 vector logos are attached to the design brief.

```html
<!DOCTYPE html>
<html lang="en">
<head>
<meta charset="utf-8">
<title>Tallmoor Signs – Business Card</title>
<link rel="stylesheet" href="https://fonts.googleapis.com/css2?family=Montserrat:wght@400;500;700;800&display=swap">
<style>
  :root {
    --orange: #f37122;
    --orange-mid: #f68d4e;
    --orange-light: #f9ba93;
    --charcoal: #3a3a3c;
    --charcoal-deep: #2b2b2d;
    --ink: #333333;
    --paper: #ffffff;
    --stage: #e9e7e4;
  }
  * { box-sizing: border-box; margin: 0; padding: 0; }
  html, body {
    width: 1200px; height: 900px; overflow: hidden;
    background: var(--stage);
    font-family: "Montserrat", sans-serif;
  }
  .canvas { position: relative; width: 1200px; height: 900px; }
  .card {
    position: absolute; left: 250px; width: 700px; height: 400px;
    border-radius: 4px; overflow: hidden;
    box-shadow: 0 10px 30px rgba(0,0,0,.18);
  }

  /* Back card */
  .card-back { top: 35px; background: var(--charcoal); color: var(--paper); }
  .card-back .brand-name {
    position: absolute; top: 110px; left: 0; width: 100%;
    text-align: center; font-weight: 800; font-size: 62px;
    color: var(--orange); letter-spacing: 1px;
  }
  .card-back .services {
    position: absolute; top: 230px; left: 0; width: 100%;
    text-align: center; font-size: 15.5px; font-weight: 500; line-height: 1.65;
  }
  .services .dot { color: var(--orange); margin: 0 6px; }

  /* Front card */
  .card-front { top: 465px; background: var(--paper); }
  .swoosh { position: absolute; left: 0; top: 0; width: 700px; height: 400px; z-index: 0; }
  .card-front .brand-name {
    position: absolute; top: 150px; left: 50px; z-index: 1;
    font-weight: 800; font-size: 40px; color: var(--orange);
  }
  .card-front .divider {
    position: absolute; left: 390px; top: 48px; width: 1.5px; height: 176px;
    background: var(--orange); z-index: 1;
  }
  .contact { position: absolute; left: 412px; top: 48px; color: var(--ink); z-index: 1; }
  .contact .person { font-size: 22px; font-weight: 700; color: var(--orange); margin-bottom: 8px; }
  .contact .address { font-size: 15px; line-height: 1.45; margin-bottom: 12px; }
  .contact .line { display: flex; align-items: center; gap: 8px; font-size: 15px; line-height: 1.5; }
  .contact .line svg { width: 14px; height: 14px; flex: none; }
  .website {
    position: absolute; left: 70px; bottom: 16px; z-index: 1;
    font-size: 20px; font-weight: 500; color: var(--paper);
  }
  .website .accent { color: var(--orange); }
</style>
</head>
<body>
<main class="canvas">

  <section class="card card-back">
    <div class="brand-name">Tallmoor Wraps</div>
    <div class="services">
      <div>Large Format Graphics Printing &amp; Installations</div>
      <div>Event Graphics<span class="dot">•</span>Banners<span class="dot">•</span>Posters<span class="dot">•</span>Vehicle Fleet Graphics<span class="dot">•</span>Boat Wraps</div>
      <div>Wall Murals<span class="dot">•</span>Decals<span class="dot">•</span>Displays<span class="dot">•</span>Signs<span class="dot">•</span>Plaques<span class="dot">•</span>Digital Signs</div>
    </div>
  </section>

  <section class="card card-front">
    <svg class="swoosh" viewBox="0 0 700 400" aria-hidden="true">
      <path d="M0,318 C260,318 520,278 700,208 L700,226 C520,294 260,334 0,334 Z" fill="var(--orange)"/>
      <path d="M0,345 C260,345 520,305 700,235 L700,400 L0,400 Z" fill="var(--charcoal-deep)"/>
    </svg>
    <div class="brand-name">Tallmoor Signs</div>
    <div class="divider"></div>
    <div class="contact">
      <div class="person">Marco Alvarez</div>
      <div class="address">1840 Harbor View Lane #2<br>Coral Point, FL 33120</div>
      <div class="line">
        <svg viewBox="0 0 24 24"><path fill="var(--orange)" d="M6.6 10.8a15 15 0 0 0 6.6 6.6l2.2-2.2a1 1 0 0 1 1-.25 11.4 11.4 0 0 0 3.6.57 1 1 0 0 1 1 1V20a1 1 0 0 1-1 1A17 17 0 0 1 3 4a1 1 0 0 1 1-1h3.5a1 1 0 0 1 1 1c0 1.25.2 2.450 .57 3.6a1 1 0 0 1-.25 1z"/></svg>
        954-555-0147
      </div>
      <div class="line">
        <svg viewBox="0 0 24 24"><rect x="6" y="2" width="12" height="20" rx="2" fill="none" stroke="var(--orange)" stroke-width="2"/><circle cx="12" cy="18" r="1.2" fill="var(--orange)"/></svg>
        786-555-0192
      </div>
      <div class="line">
        <svg viewBox="0 0 24 24"><rect x="2" y="5" width="20" height="14" rx="2" fill="var(--orange)"/><path d="M3 6l9 7 9-7" fill="none" stroke="var(--paper)" stroke-width="1.6"/></svg>
        marco@tallmoor.net
      </div>
    </div>
    <div class="website">www.<span class="accent">Tallmoorwraps</span>.com</div>
  </section>

</main>
</body>
</html>
```